30% Vinegar Modern Simplistic Label

I need a label design for a new company based in Florida called Bramble Hollow. We sell natural cleaning supplies. Our initial product is 30% Vinegar - White Distilled Vinegar is the most common type of vinegar in American households and is made from grain-based ethanol which is converted to acetic acid and diluted to preferred acidity with water. White Distilled Vinegar can be used inside and outside of the home for: cooking, canning, pickling, cleaning, laundry, automotive and gardening needs, to name a few. Our vinegar is naturally derived from corn and has no additives. We would like to see designs that use the color green and portray modern/natural/organic. Very clean, simple designs.

Target Market(s)

Environmental-thinking mother's

Industry/Entity Type

Cleaning Product

Font styles to use
Sans Serif
Script

Colors
00a990
33b8a4
86cfc6
fff3d1
fcf9ce
eaf2ce

Requirements
Must have
• 1 gallon label dimensions
• 11 x 5.5
Nice to have
• I like it to have the same feel as https://www.shopvendara.example/30-Vinegar-Concentrate-Concentrated-Industrial/dp/K42T19QXWP/ref=sr_1_3?ie=UTF8&qid=1534205686&sr=8-3&keywords=vinegar+30

```html
<!DOCTYPE html>
<html lang="en">
<head>
<meta charset="utf-8">
<title>30% Vinegar – Gallon Label</title>
<link rel="stylesheet" href="https://fonts.googleapis.com/css2?family=Caveat:wght@600&family=Amatic+SC:wght@700&family=Arimo:wght@400&display=swap">
<style>
  :root {
    --page: #f4f4f4;
    --label-light: #ffffff;
    --label-shade: #e6e6e6;
    --script-green: #2fb04a;
    --leaf-green: #5cb83a;
    --lime: #c6dc3a;
    --deep-green: #3f8f2a;
    --ink: #2b2b2b;
    --fine-ink: #8a8a8a;
    --brand-red: #c8202b;
  }
  * { box-sizing: border-box; margin: 0; padding: 0; }
  html, body { width: 1200px; height: 874px; overflow: hidden; background: var(--page); }
  .canvas { position: relative; width: 1200px; height: 874px; }
  .label {
    position: absolute; left: 50px; top: 162px; width: 1100px; height: 550px;
    background: linear-gradient(90deg, var(--label-shade) 0%, var(--label-light) 30%, var(--label-light) 70%, var(--label-shade) 100%);
    overflow: hidden;
    box-shadow: 0 6px 24px rgba(0,0,0,0.12);
  }
  .side-panel {
    position: absolute; top: 40px; width: 230px;
    font-family: "Arimo", sans-serif; font-size: 9.5px; line-height: 1.45; color: var(--fine-ink);
  }
  .side-panel p + p { margin-top: 12px; }
  .side-panel .url { word-break: break-all; }
  .side-panel--left { left: 40px; }
  .side-panel--right { right: 40px; }
  .front-panel {
    position: absolute; left: 350px; top: 0; width: 400px; height: 400px;
    display: flex; flex-direction: column; align-items: center;
  }
  .product-title {
    margin-top: 60px; font-family: "Caveat", cursive; font-weight: 600;
    color: var(--script-green); text-align: center; line-height: 0.85;
  }
  .product-title .percent { display: block; font-size: 64px; transform: rotate(-6deg); }
  .product-title .name { display: block; font-size: 96px; }
  .product-type {
    margin-top: 22px; font-family: "Amatic SC", sans-serif; font-weight: 700;
    font-size: 38px; letter-spacing: 2px; color: var(--ink);
  }
  .brand { margin-top: 12px; display: flex; align-items: center; gap: 8px; }
  .brand-dot { width: 26px; height: 26px; border-radius: 50%; background: var(--brand-red); }
  .brand-name { font-family: "Arimo", sans-serif; font-size: 22px; color: var(--brand-red); text-transform: uppercase; letter-spacing: 1px; }
  .uses {
    margin-top: 22px; font-family: "Arimo", sans-serif; font-size: 14px; line-height: 1.6;
    color: var(--ink); text-align: center;
  }
  .foliage-band { position: absolute; left: 0; bottom: 0; width: 1100px; height: 180px; }
</style>
</head>
<body>
<main class="canvas">
  <section class="label">
    <div class="side-panel side-panel--left">
      <p>I need a label design for a new company based in Florida called Bramble Hollow. We sell natural cleaning supplies. Our initial product is 30% Vinegar - White Distilled Vinegar is the most common type of vinegar in American households and is made from grain-based ethanol which is converted to acetic acid and diluted to preferred acidity with water. White Distilled Vinegar can be used inside and outside of the home for: cooking, canning, pickling, cleaning, laundry, automotive and gardening needs, to name a few. Our vinegar is naturally derived from corn and has no additives. Very clean, simple designs.</p>
      <p>Nice to have: I like it to have the same feel as <span class="url">https://www.shopvendara.example/30-Vinegar-Concentrate-Concentrated-Industrial/dp/K42T19QXWP/ref=sr_1_3?ie=UTF8&amp;qid=1534205686&amp;sr=8-3&amp;keywords=vinegar+30</span></p>
    </div>

    <div class="front-panel">
      <h1 class="product-title"><span class="percent">30%</span><span class="name">Vinegar</span></h1>
      <p class="product-type">White Distilled Vinegar</p>
      <div class="brand"><span class="brand-dot"></span><span class="brand-name">Bramble Hollow</span></div>
      <p class="uses">Cooking • Canning • Pickling • Cleaning • Laundry<br>Automotive and Gardening needs</p>
    </div>

    <div class="side-panel side-panel--right">
      <p>I need a label design for a new company based in Florida called Bramble Hollow. We sell natural cleaning supplies. Our initial product is 30% Vinegar - White Distilled Vinegar is the most common type of vinegar in American households and is made from grain-based ethanol which is converted to acetic acid and diluted to preferred acidity with water. White Distilled Vinegar can be used inside and outside of the home for: cooking, canning, pickling, cleaning, laundry, automotive and gardening needs, to name a few. Our vinegar is naturally derived from corn and has no additives. Very clean, simple designs.</p>
      <p>Nice to have: I like it to have the same feel as <span class="url">https://www.shopvendara.example/30-Vinegar-Concentrate-Concentrated-Industrial/dp/K42T19QXWP/ref=sr_1_3?ie=UTF8&amp;qid=1534205686&amp;sr=8-3&amp;keywords=vinegar+30</span></p>
    </div>

    <svg class="foliage-band" viewBox="0 0 1100 180" preserveAspectRatio="none" role="img" aria-label="Band of layered green leaves and lime waves along the bottom of the label">
      <defs>
        <linearGradient id="leafGradient" x1="0" y1="0" x2="0" y2="1">
          <stop offset="0" stop-color="#c6dc3a"/>
          <stop offset="0.5" stop-color="#5cb83a"/>
          <stop offset="1" stop-color="#3f8f2a"/>
        </linearGradient>
      </defs>
      <path d="M0 40 C 300 110, 700 0, 1100 40 L1100 180 L0 180 Z" fill="url(#leafGradient)"/>
      <path d="M0 50 C 320 120, 720 10, 1100 50" fill="none" stroke="#ffffff" stroke-width="6" opacity="0.9"/>
      <path d="M0 80 C 360 150, 740 40, 1100 90" fill="none" stroke="#eaf2ce" stroke-width="3" opacity="0.7"/>
    </svg>
  </section>
</main>
</body>
</html>
```